Book Cover Design Project

I need a book cover for my new upcoming book called "Silent Tee Stance".
The book is mental golf book and all about how the subconscious mind drives your decisions, emotions and actions.
I want a head or skull or brain design with a fairway placed inside the logo.
Also thinking a design of a landscape of a golf hole in the mind logo.. Just throwing our ideas to your designers
Thanks

Reason: I want to invite other designers

Reason: I would like to invite more designers to the project

Reason: Not getting designs I am looking for .

Reason: Designs not ready

Reason: need further design work on current designs

Reason: finalizing drafts :)

Reason: working with one designer to finalize book cover

Target Market(s)

golfers who want to find their true peak performance and people who want to improve their own lives and personal performance

Industry/Entity Type

Landscape

Requirements
Must have
• golf in mind
brain design
fairway design
Nice to have
• golf on cover

```html
<!DOCTYPE html>
<html lang="en">
<head>
<meta charset="utf-8">
<title>Silent Tee Stance – Book Cover</title>
<link rel="stylesheet" href="https://fonts.googleapis.com/css2?family=Oswald:wght@600;700&family=Roboto+Condensed:wght@700&display=swap">
<style>
  :root {
    --stage: #d6d6d6;
    --paper: #e4e4e4;
    --spine: #dcdcdc;
    --ink: #111111;
    --title-shadow: #8a8a8a;
    --art-light: #d0d0d0;
    --art-dark: #2a2a2a;
    --box-text: #9a9a9a;
  }
  * { box-sizing: border-box; margin: 0; padding: 0; }
  html, body { width: 1200px; height: 800px; overflow: hidden; }
  body {
    background: var(--stage);
    font-family: "Roboto Condensed", "Arial Narrow", sans-serif;
    color: var(--ink);
  }
  .cover-spread {
    position: absolute;
    left: 170px;
    top: 85px;
    height: 630px;
    display: flex;
    box-shadow: 0 6px 24px rgba(0,0,0,0.18);
  }
  .back-cover, .front-cover {
    width: 415px;
    height: 100%;
    background: var(--paper);
    position: relative;
    overflow: hidden;
  }
  .spine {
    width: 30px;
    height: 100%;
    background: var(--spine);
    display: flex;
    flex-direction: column;
    align-items: center;
    padding: 14px 0;
    gap: 22px;
    border-left: 1px solid #c8c8c8;
    border-right: 1px solid #c8c8c8;
  }
  .spine-title, .spine-author {
    writing-mode: vertical-rl;
    font-family: "Oswald", "Arial Narrow", sans-serif;
    font-weight: 700;
    text-transform: uppercase;
    white-space: nowrap;
  }
  .spine-title { font-size: 24px; letter-spacing: 0.5px; text-shadow: 2px 1px 0 var(--title-shadow); }
  .spine-author { font-size: 11px; letter-spacing: 0.5px; }

  .book-title {
    font-family: "Oswald", "Arial Narrow", sans-serif;
    font-weight: 700;
    text-transform: uppercase;
    line-height: 1;
    text-shadow: 3px 2px 0 var(--title-shadow);
    white-space: nowrap;
  }
  .author-name {
    font-family: "Roboto Condensed", "Arial Narrow", sans-serif;
    font-weight: 700;
    text-transform: uppercase;
  }

  /* Back cover */
  .back-cover { padding: 26px 30px 0 32px; }
  .back-cover .author-name { text-align: right; font-size: 15px; margin-bottom: 2px; }
  .back-cover .book-title { font-size: 43px; margin-bottom: 14px; }
  .blurb {
    font-size: 12.4px;
    line-height: 1.55;
    text-align: justify;
    height: 398px;
    overflow: hidden;
  }
  .back-boxes {
    position: absolute;
    left: 32px; right: 30px; bottom: 30px;
    display: flex;
    justify-content: space-between;
  }
  .placeholder-box {
    width: 112px;
    height: 46px;
    background: var(--ink);
    color: var(--box-text);
    font-size: 10px;
    display: flex;
    align-items: center;
    justify-content: center;
    text-transform: uppercase;
  }

  /* Front cover */
  .front-cover .book-title {
    position: absolute;
    top: 32px; left: 0; right: 0;
    text-align: center;
    font-size: 50px;
  }
  .cover-art {
    position: absolute;
    left: 60px; top: 112px;
    width: 330px; height: 450px;
  }
  .front-cover .author-name {
    position: absolute;
    bottom: 22px; left: 0; right: 0;
    text-align: center;
    font-size: 21px;
  }
</style>
</head>
<body>
  <main class="cover-spread">
    <section class="back-cover">
      <p class="author-name">Author Name</p>
      <h2 class="book-title">Silent Tee Stance</h2>
      <p class="blurb">Lorem ipsum dolor sit amet, consectetur adipisicing elit, sed do eiusmod tempor incididunt ut labore et dolore magna aliqua. Ut enim ad minim veniam, quis nostrud exercitation. Lorem ipsum dolor sit amet, consectetur adipisicing elit, sed do eiusmod tempor incididunt ut labore et dolore magna aliqua. Ut enim ad minim veniam, quis nostrud exercitation. Lorem ipsum dolor sit amet, consectetur adipisicing elit, sed do eiusmod tempor incididunt ut labore et dolore magna aliqua. Ut enim ad minim veniam, quis nostrud exercitation. Lorem ipsum dolor sit amet, consectetur adipisicing elit, sed do eiusmod tempor incididunt ut labore et dolore magna aliqua. Ut enim ad minim veniam, quis nostrud exercitation. Lorem ipsum dolor sit amet, consectetur adipisicing elit, sed do eiusmod tempor incididunt ut labore et dolore magna aliqua. Ut enim ad minim veniam, quis nostrud exercitation. Lorem ipsum dolor sit amet, consectetur adipisicing elit, sed do eiusmod tempor incididunt ut labore et dolore magna aliqua. Ut enim ad minim veniam, quis nostrud exercitation. Lorem ipsum dolor sit amet, consectetur adipisicing elit, sed do eiusmod tempor incididunt ut labore et dolore magna aliqua. Ut enim ad minim veniam, quis nostrud exercitation. Lorem ipsum dolor sit amet, consectetur adipisicing elit, sed do eiusmod tempor incididunt ut labore et dolore magna aliqua. Ut enim ad minim veniam, quis nostrud exercitation.</p>
      <div class="back-boxes">
        <div class="placeholder-box">Logo</div>
        <div class="placeholder-box">ISBN</div>
      </div>
    </section>

    <section class="spine">
      <span class="spine-title">Silent Tee Stance</span>
      <span class="spine-author">Author Name</span>
    </section>

    <section class="front-cover">
      <h1 class="book-title">Silent Tee Stance</h1>
      <svg class="cover-art" viewBox="0 0 330 450" role="img" aria-label="Black ink illustration of a golfer's head in profile with the top opened, an exposed brain forming a landscape where small golfers swing beside a flagstick">
        <defs>
          <radialGradient id="art-tone" cx="50%" cy="55%" r="60%">
            <stop offset="0%" stop-color="var(--art-dark)"/>
            <stop offset="100%" stop-color="var(--art-light)"/>
          </radialGradient>
        </defs>
        <rect width="330" height="450" fill="url(#art-tone)" opacity="0.55"/>
      </svg>
      <p class="author-name">Author Name</p>
    </section>
  </main>
</body>
</html>
```